HVAC Contractor Website Design

We are working with an HVAC contractor in Idaho called KR HVAC.
Some sites to use for content/competitors and inspiration:
https://www.brelvoclimate.com
https://pinemarsh.site/web/contractor/ (lots of contractor website designs we've approved and continue to show clients)
Thank you for taking the time to consider designing a website for us. We are web developers based in Stockton, CA, USA. Most of our projects go through the same process. Understanding this process may help you win a project with us. We custom-code all of our websites in-house. We don’t have any requirements as to what tools you use for your design, but we prefer Figma files. For any design that we label as four-stars, we send it to the client for review. The client picks the final design they want us to use. Once we complete this process, we will continue to show additional clients all the four-star sites and purchase them later. Your designs will have multiple chances to sell. For better chances of success, we ask that you follow these guidelines.
IMAGES:
If you use any images or icons in the design, we ask that you have a link to the asset so we can purchase the image/icon. Most of the designs we submit do not have the customer’s images on them unless they have some great images. Be creative; show us the feeling you are trying to portray with your image choices. Use any royalty-free site you choose. We subscribe to Adobe and mainly use their images, but we can purchase images outside of Adobe.
PLEASE NOTE: we will not submit designs to clients with watermarks on the images.
FONTS:
We ask that you identify the fonts used in the design. This can be done in a message if you want. We typically use Google Fonts and Adobe Fonts.
CONTENT:
We're always open to different content and ideas. We often submit designs with stock images so the client can see our vision. We typically take pictures after the website launch to use their images with our vision. Lorem Ipsum is fine for paragraphs, but we ask that you write the headers in correct English. We want to be able to show the vision and identify the sections of the website.
INSPIRATION:
We typically add a couple of links in the brief of websites we like to help you get started in your design.
REVISIONS:
We do not often ask for revisions of the designs unless we see something in the design that may not appeal to the client. If there are slight changes that we want to make, we do that in the development process.
FEEDBACK:
We rarely give feedback on designs during the design process. We are working on many website projects and do not have the time to provide feedback. We usually respond if your request is well thought out and asks specific questions, but a note asking “feedback, please” usually goes unanswered

```html
<!DOCTYPE html>
<html lang="en">
<head>
<meta charset="utf-8">
<title>KR HVAC – Heating &amp; Cooling</title>
<link href="https://fonts.googleapis.com/css2?family=Poppins:wght@500;600;700;800&family=Lato:wght@400;700&display=swap" rel="stylesheet">
<style>
:root{
  --red:#f21b1b;
  --orange:#f26a21;
  --blue:#1565c0;
  --sky:#4fa6ff;
  --navy:#0d2a5e;
  --navy-deep:#0a2257;
  --ink:#141414;
  --text:#555a66;
  --light:#eef1f8;
  --field:#e4e6ea;
  --white:#ffffff;
}
*{margin:0;padding:0;box-sizing:border-box}
html,body{width:1200px;height:3950px;overflow:hidden}
body{font-family:'Lato',sans-serif;color:var(--text);background:var(--white);position:relative}
.abs{position:absolute}
section,header{position:relative;width:1200px}
h1,h2,h3,h4,.head{font-family:'Poppins',sans-serif;color:var(--ink)}

/* top bar */
.topbar{height:38px;background:var(--blue);color:var(--white);font-size:12px}
.topbar .item{top:11px;display:flex;align-items:center;gap:7px}
.topbar .dot{top:8px;width:22px;height:22px;border-radius:50%;background:var(--white)}

/* hero */
.hero{height:713px;background:linear-gradient(180deg,#0e2a66 0%,#0b2660 55%,#0a2257 100%)}
.brand{display:flex;align-items:center;gap:8px;font-family:'Poppins',sans-serif;font-weight:700;color:var(--white)}
.brand .mark{width:14px;height:14px;border-radius:50%;background:var(--red)}
.nav{display:flex;font-family:'Poppins',sans-serif;font-size:12px;font-weight:500;color:var(--white)}
.nav a{position:absolute;white-space:nowrap;color:var(--white);text-decoration:none}
.nav a.active{color:var(--red)}
.nav a.active::after{content:"";position:absolute;left:-6px;right:-6px;top:28px;height:2px;background:var(--sky)}
.search{left:1127px;width:40px;height:40px;border-radius:50%;background:var(--red)}
.hero .kicker{left:70px;font-family:'Poppins',sans-serif;font-size:34px;font-weight:500;color:var(--sky)}
.hero h1{left:70px;font-size:52px;font-weight:800;color:var(--white)}
.hero p{left:74px;width:440px;font-size:12px;line-height:27px;color:#dbe3f3}
.btn{display:flex;align-items:center;justify-content:center;font-family:'Poppins',sans-serif;font-size:12px;font-weight:600;color:var(--white);text-transform:uppercase}
.btn-red{background:var(--red)}
.btn-ghost{border:2px solid var(--white)}
.hero-art{left:567px;width:560px;height:560px;border-radius:40% 40% 0 0;background:linear-gradient(160deg,#2a55a8,#183f8a)}

/* features */
.features{left:100px;top:713px;width:1002px;height:115px;background:var(--white);border:1px solid #e6e8ee;box-shadow:0 8px 24px rgba(0,0,0,.06);display:flex}
.feature{position:relative;flex:1}
.feature .ic{position:absolute;left:35px;top:22px;width:68px;height:70px;border:3px solid #222;border-radius:8px}
.feature h3{position:absolute;left:131px;top:26px;font-size:18px;font-weight:600}
.feature p{position:absolute;left:131px;top:56px;width:260px;font-size:12px;line-height:21px}

/* about */
.about{height:943px}
.about .worker{left:46px;top:222px;width:284px;height:593px;background:linear-gradient(180deg,#1f57c9,#1a49a8 70%,#c9a46a)}
.about .frame{left:360px;top:245px;width:265px;height:577px;border:11px solid #f2454a}
.about .unit{left:371px;top:256px;width:243px;height:555px;background:linear-gradient(180deg,#cfd4da,#e8eaec 60%,#9aa592)}
.badge{left:340px;top:325px;width:141px;height:122px;background:var(--navy);border-radius:8px;color:var(--white);text-align:center}
.badge b{display:block;font-family:'Poppins',sans-serif;font-size:44px;line-height:44px;margin-top:10px}
.badge span{display:block;font-size:13px;line-height:16px;margin-top:4px}
.label{display:flex;align-items:center;gap:10px;font-size:11px;text-transform:uppercase;color:#666}
.label i{display:block;height:2px;background:var(--red)}
.about h2{left:667px;top:307px;font-size:27px;line-height:33px;font-weight:700}
.about p.copy{left:669px;width:460px;font-size:12px;line-height:26px}
.point{width:230px}
.point .ic{position:absolute;left:0;top:0;width:40px;height:40px}
.point h4{margin-left:52px;font-size:13px;font-weight:600}
.point p{margin-left:52px;font-size:12px;line-height:21px;text-align:justify;margin-top:4px}

/* services */
.services{height:682px;background:linear-gradient(180deg,#eceff7,#f1f3f9)}
.services h2{left:87px;top:110px;font-size:40px;font-weight:700}
.services .intro{left:684px;top:115px;width:480px;font-size:13px;line-height:26px}
.card{top:208px;width:240px;height:305px;background:var(--white);border-bottom:3px solid var(--red);text-align:center;box-shadow:0 4px 14px rgba(0,0,0,.05)}
.card svg{margin-top:42px}
.card h3{margin-top:16px;font-size:16px;font-weight:600;color:var(--navy)}
.card p{margin:12px 20px 0;font-size:12px;line-height:21px;text-align:justify;text-align-last:center}
.card .more{display:block;margin-top:26px;font-family:'Poppins',sans-serif;font-size:11px;font-weight:600;letter-spacing:1.5px;color:var(--red)}
.arrow{top:334px;width:44px;height:44px;border-radius:50%;border:1px solid #c8ccd6;background:var(--white)}
.pager{top:581px;height:2px;width:32px;background:#cfd3dc}

/* quote */
.quote{height:486px;background:var(--blue);color:var(--white)}
.quote .small{left:245px;top:115px;font-family:'Poppins',sans-serif;font-size:13px;letter-spacing:1.5px}
.quote h2{left:245px;top:145px;font-size:34px;font-weight:700;color:var(--white)}
.type{top:102px;width:100px;height:99px;border-radius:12px;background:#e8eaee;color:#333;font-size:12px;font-weight:700;text-align:center}
.type.on{background:var(--red);color:var(--white)}
.type svg{margin-top:20px}
.type span{display:block;margin-top:8px}
.field{height:42px;background:var(--field);border-radius:4px;color:#444;font-size:12px;display:flex;align-items:center;padding:0 22px;justify-content:space-between}

/* partners */
.partners{height:135px;background:#f4f5f9}
.partner{top:50px;height:34px;width:110px;border-radius:17px;background:#c9cce0}

/* testimonials */
.testimonials{height:524px}
.testimonials h2{left:116px;top:125px;font-size:40px;font-weight:700}
.review{top:202px;width:472px;height:204px;background:var(--white);box-shadow:0 6px 24px rgba(0,0,0,.08)}
.review .face{position:absolute;left:20px;top:44px;width:118px;height:118px;border-radius:50%;background:linear-gradient(160deg,#d9c4b0,#8d6a55)}
.review p{position:absolute;left:158px;top:44px;width:290px;font-size:12px;line-height:22px}
.review h4{position:absolute;left:158px;top:128px;font-size:14px;font-weight:600;color:var(--navy)}
.review small{position:absolute;left:158px;top:152px;font-size:11px}
.review .qm{position:absolute;right:42px;top:128px;font-family:'Poppins',sans-serif;font-size:80px;line-height:80px;color:#dfe3ee}
.tdot{top:3421px;width:9px;height:9px;border-radius:50%;background:#d6dbe8}

/* contact bar & footer */
.contact{height:97px;background:#0e2c68;color:var(--white)}
.contact .item{top:28px;display:flex;align-items:center;gap:20px;font-size:12px;line-height:20px}
.contact .ic{width:48px;height:48px;border-radius:8px;background:rgba(255,255,255,.1);display:flex;align-items:center;justify-content:center}
.contact b{font-size:16px}
.contact .sep{top:0;width:1px;height:97px;background:rgba(255,255,255,.15)}
.footer{height:370px;background:var(--navy-deep);color:#d7def0}
.footer h4{font-size:16px;font-weight:600;color:var(--white)}
.footer ul{list-style:none;font-size:13px;line-height:29px;margin-top:14px}
.footer .social{top:216px;width:22px;height:22px;border-radius:50%;background:rgba(255,255,255,.12)}
.footer .rule{left:87px;top:306px;width:1090px;height:1px;background:rgba(255,255,255,.15)}
</style>
</head>
<body>

<!-- top bar -->
<div class="topbar abs" style="top:0;left:0;width:1200px">
  <div class="item abs" style="left:34px">
    <svg width="12" height="12" viewBox="0 0 24 24" fill="none" stroke="#fff" stroke-width="2.4"><path d="M5 3h4l2 5-3 2a12 12 0 0 0 6 6l2-3 5 2v4a2 2 0 0 1-2 2A17 17 0 0 1 3 5a2 2 0 0 1 2-2z"/></svg>+1(208) 555 0147</div>
  <div class="item abs" style="left:214px">
    <svg width="13" height="10" viewBox="0 0 26 20" fill="#fff"><path d="M0 0h26v20H0z"/></svg>info@krhvac.com</div>
  <span class="dot abs" style="left:1041px"></span>
  <span class="dot abs" style="left:1074px"></span>
  <span class="dot abs" style="left:1108px"></span>
  <span class="dot abs" style="left:1142px"></span>
</div>

<!-- hero -->
<header class="hero abs" style="top:38px;left:0">
  <div class="brand abs" style="left:31px;top:30px;font-size:40px"><span class="mark"></span>KR HVAC</div>
  <nav class="nav abs" style="top:46px;left:0">
    <a class="active" style="left:352px">HOME</a>
    <a style="left:429px">ABOUT US</a>
    <a style="left:526px">ALL SERVICES +</a>
    <a style="left:655px">SERVICE AREAS +</a>
    <a style="left:796px">CAREERS</a>
    <a style="left:889px">CONTACT US</a>
  </nav>
  <div class="search abs" style="top:34px">
    <svg class="abs" style="left:11px;top:11px" width="18" height="18" viewBox="0 0 24 24" fill="none" stroke="#fff" stroke-width="3"><circle cx="10" cy="10" r="7"/><path d="M15 15l6 6"/></svg>
  </div>
  <div class="hero-art abs" style="top:115px" role="img" aria-label="Cartoon repairman holding a pipe wrench and spanner"></div>
  <div class="kicker abs" style="top:254px">Trusted Repair &amp; Servicing</div>
  <h1 class="abs" style="top:292px">At Your Door Step</h1>
  <p class="abs" style="top:372px">Lorem ipsum dolor sit amet, consectetur adipiscing elit, sed do eiusmod tempor incididunt ut labore et dolore magna aliqua. Quis ipsum suspendisse ultrices gravida. Risus commodo viverra maecenas accumsan lacus vel facilisis.</p>
  <div class="btn btn-red abs" style="left:72px;top:483px;width:129px;height:38px">Know More</div>
  <div class="btn btn-ghost abs" style="left:213px;top:483px;width:129px;height:38px">Get A Quote</div>
</header>

<div class="features abs">
  <div class="feature">
    <div class="ic" role="img" aria-label="Engineer icon" style="border:none;background:#f3f3f5"></div>
    <h3>Qualified Engineers</h3>
    <p>In house Ac Technicians with 10+ years of experience</p>
  </div>
  <div class="feature">
    <svg class="ic" style="border:none" width="68" height="70" viewBox="0 0 68 70" fill="none" stroke="#222" stroke-width="3"><rect x="6" y="14" width="56" height="46" rx="4"/><path d="M24 14V6h20v8M6 32h56"/><rect x="18" y="24" width="32" height="16" stroke="#f21b1b"/></svg>
    <h3>High-Quality Repair Work</h3>
    <p>High-Quality AC Spares, 90-day warranty on spare parts &amp; 30-day warranty on service</p>
  </div>
</div>

<!-- about -->
<section class="about abs" style="top:713px;left:0">
  <div class="worker abs" role="img" aria-label="Technician in blue overalls pointing at the unit"></div>
  <div class="frame abs"></div>
  <div class="unit abs" role="img" aria-label="Outdoor air conditioning unit beside a house"></div>
  <div class="badge abs"><b>30</b><span>Years of<br>Experience in<br>this Field</span></div>
  <div class="label abs" style="left:667px;top:281px"><i style="width:66px"></i>Know About Us</div>
  <h2 class="abs">Air Conditioning Repair,<br>Heating Service &amp; Installation</h2>
  <p class="copy abs" style="top:404px">The best way to provide the highest quality level of care requires an initial meeting where family and/or client meet with a Visiting CareGiver coordinator. This meeting includes a detailed review of care needed, schedule.</p>
  <p class="copy abs" style="top:511px">Specific physical needs of the care recipient with regards to bathing and grooming, dressing, meals and diet, mobility, and incontinence.</p>
  <div class="point abs" style="left:668px;top:598px">
    <svg class="ic" viewBox="0 0 40 40" fill="none" stroke="#333" stroke-width="2"><path d="M4 18h8v18H4zM12 20l8-14c3 0 4 2 3 6l-2 6h12c2 0 3 2 2 4l-4 12H12"/></svg>
    <h4>Top Rated Service</h4>
    <p>Lorem ipsum dolor sit amet, consectetur adipiscing elit, sed do eiusmod tempor incididunt ut labore</p>
  </div>
  <div class="point abs" style="left:924px;top:598px">
    <svg class="ic" viewBox="0 0 40 40" fill="none" stroke="#333" stroke-width="2"><circle cx="20" cy="21" r="15"/><path d="M20 12v9l6 4" stroke="#f21b1b"/></svg>
    <h4>Top Rated Service</h4>
    <p>Lorem ipsum dolor sit amet, consectetur adipiscing elit, sed do eiusmod tempor incididunt ut labore</p>
  </div>
  <div class="btn btn-red abs" style="left:670px;top:743px;width:129px;height:37px">Know More</div>
</section>

<!-- services -->
<section class="services abs" style="top:1656px;left:0">
  <div class="label abs" style="left:89px;top:86px"><i style="width:66px"></i>Our Services</div>
  <h2 class="abs">What We Do</h2>
  <p class="intro abs">Bring to the table win-win survival strategies to ensure proactive domination. At the end of the day, going forward.</p>
  <div class="arrow abs" style="left:33px"><svg class="abs" style="left:17px;top:16px" width="10" height="12" viewBox="0 0 10 12" fill="none" stroke="#888" stroke-width="1.5"><path d="M7 1L2 6l5 5"/></svg></div>
  <div class="arrow abs" style="left:1140px"><svg class="abs" style="left:17px;top:16px" width="10" height="12" viewBox="0 0 10 12" fill="none" stroke="#888" stroke-width="1.5"><path d="M3 1l5 5-5 5"/></svg></div>
  <div class="card abs" style="left:87px">
    <svg width="56" height="56" viewBox="0 0 56 56" fill="none" stroke="#1565c0" stroke-width="2"><rect x="4" y="6" width="40" height="40" rx="3"/><circle cx="24" cy="26" r="12"/><path d="M44 20h8v30M24 14v24M12 26h24"/></svg>
    <h3>Heating Services</h3>
    <p>Lorem ipsum dolor sit amet, consectetur adipiscing elit, sed do eiusmod tempor inc-</p>
    <span class="more">READ MORE</span>
  </div>
  <div class="card abs" style="left:354px">
    <svg width="56" height="56" viewBox="0 0 56 56" fill="none" stroke="#1565c0" stroke-width="2"><rect x="2" y="26" width="52" height="18" rx="3"/><path d="M8 36h40M14 4v18M40 4v18M10 50h4M22 50h4M34 50h4"/></svg>
    <h3>AC Maintenance</h3>
    <p>Lorem ipsum dolor sit amet, consectetur adipiscing elit, sed do eiusmod tempor inc-</p>
    <span class="more">READ MORE</span>
  </div>
  <div class="card abs" style="left:621px">
    <svg width="56" height="56" viewBox="0 0 56 56" fill="none" stroke="#1565c0" stroke-width="2"><rect x="2" y="6" width="52" height="16" rx="3"/><circle cx="22" cy="38" r="12"/><path d="M22 26v24M10 38h24M14 30l16 16M30 30L14 46"/></svg>
    <h3>AC Installation</h3>
    <p>Lorem ipsum dolor sit amet, consectetur adipiscing elit, sed do eiusmod tempor inc-</p>
    <span class="more">READ MORE</span>
  </div>
  <div class="card abs" style="left:888px">
    <svg width="56" height="56" viewBox="0 0 56 56" fill="none" stroke="#1565c0" stroke-width="2"><rect x="2" y="4" width="52" height="18" rx="4"/><path d="M10 14h36M18 28v8M28 28v10M38 28v8M16 44l6 6M22 44l-6 6M34 44l6 6M40 44l-6 6"/></svg>
    <h3>Indoor Air Quality</h3>
    <p>Lorem ipsum dolor sit amet, consectetur adipiscing elit, sed do eiusmod tempor inc-</p>
    <span class="more">READ MORE</span>
  </div>
  <span class="pager abs" style="left:531px;background:#7d8494"></span>
  <span class="pager abs" style="left:570px"></span>
  <span class="pager abs" style="left:609px"></span>
  <span class="pager abs" style="left:648px"></span>
</section>

<!-- quote -->
<section class="quote abs" style="top:2338px;left:0">
  <svg class="abs" style="left:100px;top:92px" width="108" height="110" viewBox="0 0 108 110" fill="none" stroke="#fff" stroke-width="3"><path d="M6 6h56l16 16v82H6z"/><path d="M62 6v16h16M20 40h40M20 56h36M20 72h28M20 88h20"/><path d="M100 40l-44 52-6 14 14-6 44-52z"/></svg>
  <div class="small abs">FOR FREE ESTIMATE</div>
  <h2 class="abs">Request A Quote</h2>
  <div class="abs" style="left:607px;top:88px;width:1px;height:122px;background:rgba(255,255,255,.5)"></div>
  <div class="type on abs" style="left:664px"><svg width="36" height="36" viewBox="0 0 36 36" fill="none" stroke="#fff" stroke-width="2"><path d="M4 34h28M8 34V14h8v20M16 34V6h12v28M20 12h4M20 18h4M20 24h4"/></svg><span>Commercial</span></div>
  <div class="type abs" style="left:784px"><svg width="36" height="36" viewBox="0 0 36 36" fill="none" stroke="#555" stroke-width="2"><path d="M4 34h28M8 34V6h20v28M12 12h12M12 18h12M12 24h12"/></svg><span>Residential</span></div>
  <div class="type abs" style="left:904px"><svg width="36" height="36" viewBox="0 0 36 36" fill="none" stroke="#555" stroke-width="2"><path d="M4 34h28M12 34V4h12v30M16 10h4M16 16h4M16 22h4"/></svg><span>Individual</span></div>
  <div class="type abs" style="left:1024px"><svg width="36" height="36" viewBox="0 0 36 36" fill="none" stroke="#555" stroke-width="2"><path d="M4 34h28M6 16L18 6l12 10M8 16v18M28 16v18M14 22h8v12h-8z"/></svg><span>Others</span></div>
  <div class="abs" style="left:28px;top:239px;width:1145px;height:1px;background:rgba(255,255,255,.4)"></div>
  <div class="field abs" style="left:80px;top:280px;width:337px">Your Name *</div>
  <div class="field abs" style="left:438px;top:280px;width:338px">Email Address *</div>
  <div class="field abs" style="left:797px;top:280px;width:337px">Office Address</div>
  <div class="field abs" style="left:80px;top:344px;width:337px">Select Your Work Type<svg width="10" height="6" viewBox="0 0 10 6"><path d="M0 0h10L5 6z" fill="#333"/></svg></div>
  <div class="field abs" style="left:438px;top:344px;width:338px">Select Date<svg width="10" height="6" viewBox="0 0 10 6"><path d="M0 0h10L5 6z" fill="#333"/></svg></div>
  <div class="field abs" style="left:797px;top:344px;width:337px;background:var(--red);color:#fff;justify-content:center">Get Estimate Quote</div>
</section>

<!-- partners -->
<section class="partners abs" style="top:2824px;left:0">
  <span class="partner abs" style="left:83px"></span>
  <span class="partner abs" style="left:272px"></span>
  <span class="partner abs" style="left:459px"></span>
  <span class="partner abs" style="left:645px"></span>
  <span class="partner abs" style="left:834px"></span>
  <span class="partner abs" style="left:1020px"></span>
</section>

<!-- testimonials -->
<section class="testimonials abs" style="top:2959px;left:0">
  <div class="label abs" style="left:118px;top:92px"><i style="width:66px"></i>Testimonials</div>
  <h2 class="abs">What Our Clients Say</h2>
  <div class="review abs" style="left:118px">
    <div class="face" role="img" aria-label="Portrait of a smiling client with glasses"></div>
    <p>Lorem ipsum dolor sit amet, consectetur adipiscing do eiusmod tempor incididunt ut labore rem ipsum dolor sit amet, consectetur.</p>
    <h4>Marcus Feldin</h4>
    <small>Designer</small>
    <span class="qm">&#8221;</span>
  </div>
  <div class="review abs" style="left:613px">
    <div class="face" role="img" aria-label="Portrait of a smiling client with blonde hair"></div>
    <p>Lorem ipsum dolor sit amet, consectetur adipiscing do eiusmod tempor incididunt ut labore rem ipsum dolor sit amet, consectetur.</p>
    <h4>Corinne Talvy</h4>
    <small>Designer</small>
    <span class="qm">&#8221;</span>
  </div>
</section>
<span class="tdot abs" style="left:572px;background:var(--blue)"></span>
<span class="tdot abs" style="left:586px"></span>
<span class="tdot abs" style="left:600px"></span>
<span class="tdot abs" style="left:614px"></span>

<!-- contact bar -->
<section class="contact abs" style="top:3483px;left:0">
  <div class="item abs" style="left:87px">
    <div class="ic"><svg width="24" height="28" viewBox="0 0 24 28" fill="none" stroke="#fff" stroke-width="2"><path d="M12 26s9-9 9-15a9 9 0 0 0-18 0c0 6 9 15 9 15z"/><circle cx="12" cy="11" r="3"/></svg></div>
    <div>No: 41 B, West Alder Street,<br>Boise, ID, USA 4508</div>
  </div>
  <span class="sep abs" style="left:434px"></span>
  <div class="item abs" style="left:487px">
    <div class="ic"><svg width="26" height="22" viewBox="0 0 26 22" fill="none" stroke="#fff" stroke-width="2"><path d="M2 9l11-7 11 7v11H2zM2 9l11 7 11-7"/></svg></div>
    <div>Email Us:<br><b>info@krhvac.com</b></div>
  </div>
  <span class="sep abs" style="left:780px"></span>
  <div class="item abs" style="left:835px">
    <div class="ic"><svg width="24" height="24" viewBox="0 0 24 24" fill="none" stroke="#fff" stroke-width="2"><path d="M5 3h4l2 5-3 2a12 12 0 0 0 6 6l2-3 5 2v4a2 2 0 0 1-2 2A17 17 0 0 1 3 5a2 2 0 0 1 2-2z"/></svg></div>
    <div>Call Us On:<br><b>+1(208) 555 0147</b></div>
  </div>
</section>

<!-- footer -->
<footer class="footer abs" style="top:3580px;left:0;width:1200px">
  <div class="brand abs" style="left:69px;top:56px;font-size:32px"><span class="mark"></span>KR HVAC</div>
  <p class="abs" style="left:66px;top:134px;width:220px;font-size:12px;line-height:21px;color:#fff">Duis ultricies libero sit amet aliquam fermentum. Nunc tincidunt mollis dui in tempor.</p>
  <span class="social abs" style="left:64px"></span>
  <span class="social abs" style="left:100px"></span>
  <span class="social abs" style="left:136px"></span>
  <span class="social abs" style="left:172px"></span>
  <div class="abs" style="left:360px;top:62px">
    <h4>Services</h4>
    <ul><li>AC Repair</li><li>AC Installation</li><li>AC Maintenance</li><li>Indoor Air Quality</li><li>Furnace Installation</li><li>Boiler Repair</li></ul>
  </div>
  <div class="abs" style="left:610px;top:62px">
    <h4>Useful Links</h4>
    <ul><li>Home</li><li>About Us</li><li>Service Areas</li><li>Careers</li><li>Testimonials</li><li>Contact Us</li></ul>
  </div>
  <div class="abs" style="left:860px;top:62px;width:250px">
    <h4>Useful Links</h4>
    <p style="margin-top:18px;font-size:12px;line-height:21px;padding-left:6px">Get $5 off when you sign up for emails with savings and tips.</p>
    <div style="margin-top:14px;height:40px;background:#fff;border-radius:3px;font-size:12px;color:#999;display:flex;align-items:center;padding-left:22px">Email address</div>
    <div class="btn" style="margin-top:12px;height:44px;background:var(--orange);border-radius:3px">Subscribe</div>
  </div>
  <div class="rule abs"></div>
  <p class="abs" style="left:87px;top:333px;font-size:11px">© Copyright 2024. All right reserved.</p>
  <div class="abs" style="left:1168px;top:230px;width:1px;height:60px;background:rgba(255,255,255,.4)"></div>
  <div class="abs" style="left:1175px;top:296px;font-size:10px;transform:rotate(90deg);transform-origin:left top;color:rgba(255,255,255,.5);white-space:nowrap">Go To Top</div>
</footer>

</body>
</html>
```